Tall Reed Software PowerPoint template

We are a software company selling endpoint visibility, access and security technology to enterprise-level IT departments.
Our technology helps organizations gain comprehensive visibility into and control over devices accessing their corporate network so they can quickly identify and address suspicious activity on the network that could lead to potential threats like data breaches.
This technology can cost organizations upwards of $1M - depending on the size of the organization. Our primary clients are Meridian 2,000 companies.
We want a professional, polished PowerPoint template that we can use for all company presentations. Please include:
Title page
Section page
General info page
Thank you page
Logo options and color specs are attached.
Please include our tagline on at least the title page: Discover the edge. Optimize the whole.

```html
<!DOCTYPE html>
<html lang="en">
<head>
<meta charset="utf-8">
<title>Tall Reed Software – Title Slide Variations</title>
<link rel="stylesheet" href="https://fonts.googleapis.com/css2?family=PT+Sans+Narrow:wght@400;700&family=Lato:ital,wght@0,400;0,700;1,700&display=swap">
<style>
  :root {
    --stage: #1c1f21;
    --red: #a5161b;
    --red-light: #b8262b;
    --red-deep: #7d0c10;
    --maroon: #8c1a1f;
    --copper: #d4835e;
    --copper-dark: #b5603c;
    --graphite-light: #6b6b6b;
    --graphite-dark: #3a3a3a;
    --blush-light: #fdf1ec;
    --blush: #f2cfc5;
    --paper: #fbf6f6;
    --cream: #fcf9e8;
    --white: #ffffff;
    --ink-grey: #6d6d6d;
  }
  * { box-sizing: border-box; margin: 0; padding: 0; }
  html, body { width: 1200px; height: 900px; overflow: hidden; background: var(--stage); }
  .board { position: relative; width: 1200px; height: 900px; }

  .slide {
    position: absolute; width: 586px; height: 438px; overflow: hidden;
    font-family: "PT Sans Narrow", "Arial Narrow", sans-serif;
  }
  .slide--a { left: 10px; top: 8px; }
  .slide--b { left: 604px; top: 8px; }
  .slide--c { left: 10px; top: 454px; }
  .slide--d { left: 604px; top: 454px; }

  .slide__header { position: absolute; left: 0; top: 0; width: 100%; height: 258px; }
  .slide--graphite .slide__header { background: radial-gradient(ellipse at 55% 20%, var(--graphite-light), var(--graphite-dark) 80%); }
  .slide--crimson .slide__header { background: radial-gradient(ellipse at 55% 20%, var(--red-light), var(--red) 55%, #8e1216 100%); }
  .slide--blush .slide__header { background: radial-gradient(ellipse at 55% 40%, var(--blush-light), var(--blush) 90%); }

  .slide__rule { position: absolute; left: 0; top: 258px; width: 100%; height: 4px; background: var(--copper); }

  .slide__body { position: absolute; left: 0; top: 262px; width: 100%; height: 134px; background: linear-gradient(180deg, var(--white), var(--paper)); }
  .slide--d .slide__body { background: linear-gradient(180deg, #fffdf3, var(--cream)); }

  .slide__title {
    position: absolute; right: 34px; top: 92px; text-align: right;
    font-weight: 700; font-size: 33px; line-height: 1; color: var(--white);
  }
  .slide__subtitle {
    position: absolute; right: 34px; top: 140px; width: 360px; text-align: right;
    font-size: 14px; line-height: 19px; color: #f3e6e6;
  }
  .slide--blush .slide__title { color: var(--maroon); }
  .slide--blush .slide__subtitle { color: var(--maroon); }
  .slide--d .slide__title { right: 0; left: 0; text-align: center; top: 104px; font-size: 36px; }
  .slide--d .slide__subtitle { right: 0; left: 0; width: auto; text-align: center; top: 156px; font-size: 15px; line-height: 21px; }

  .portrait { position: absolute; left: 20px; top: 152px; width: 212px; height: 212px; }

  .brand {
    position: absolute; right: 28px; top: 316px;
    display: flex; align-items: center; gap: 12px;
    font-family: "Lato", sans-serif; font-weight: 400; font-size: 23px;
    letter-spacing: 1px; color: var(--maroon);
  }
  .slide--d .brand { right: auto; left: 50%; transform: translateX(-50%); }
  .brand__dot { width: 16px; height: 16px; border-radius: 50%; background: var(--copper); }

  .footer {
    position: absolute; left: 0; bottom: 0; width: 100%; height: 42px;
    border-top: 3px solid var(--copper);
    background: linear-gradient(180deg, #c8191e, var(--red) 50%, var(--red-deep));
    font-family: "Lato", sans-serif; color: var(--white);
  }
  .footer__page {
    position: absolute; left: 16px; top: 8px; width: 30px; height: 25px;
    background: linear-gradient(180deg, #e07a45, #b94a1f); border-radius: 2px;
    font-size: 15px; line-height: 25px; text-align: center;
  }
  .footer__date { position: absolute; left: 92px; top: 12px; font-size: 14px; font-weight: 700; font-style: italic; }
  .footer__start {
    position: absolute; right: 14px; top: 6px; width: 48px; height: 27px;
    background: linear-gradient(180deg, #ec9a62, #c9571f);
    clip-path: polygon(0 0, 78% 0, 100% 50%, 78% 100%, 0 100%);
    border-radius: 2px; font-size: 11px; line-height: 27px; padding-left: 8px;
  }
</style>
</head>
<body>
<main class="board">

  <section class="slide slide--a slide--graphite">
    <div class="slide__header"></div>
    <div class="slide__rule"></div>
    <div class="slide__body"></div>
    <h1 class="slide__title">Project Title Here</h1>
    <p class="slide__subtitle">Subtext here Subtext here Subtext here Subtext here Subtext here Subtext here Subtext here Subtext here</p>
    <svg class="portrait" viewBox="0 0 212 212" role="img" aria-label="Circular portrait photo of the presenter">
      <defs><linearGradient id="photoA" x1="0" y1="0" x2="0" y2="1"><stop offset="0" stop-color="#f4f2f1"/><stop offset="0.6" stop-color="#d9c5b6"/><stop offset="1" stop-color="#3b3a3c"/></linearGradient></defs>
      <circle cx="106" cy="106" r="105" fill="#dfa588"/>
      <circle cx="106" cy="106" r="101" fill="#9a1c22"/>
      <circle cx="106" cy="106" r="96" fill="#ffffff"/>
      <circle cx="106" cy="106" r="91" fill="url(#photoA)"/>
    </svg>
    <div class="brand"><span class="brand__dot"></span>Tall Reed Software</div>
    <footer class="footer"><span class="footer__page">01</span><span class="footer__date">01/02/15</span><span class="footer__start">Start</span></footer>
  </section>

  <section class="slide slide--b slide--crimson">
    <div class="slide__header"></div>
    <div class="slide__rule"></div>
    <div class="slide__body"></div>
    <h1 class="slide__title">Project Title Here</h1>
    <p class="slide__subtitle">Subtext here Subtext here Subtext here Subtext here Subtext here Subtext here Subtext here Subtext here</p>
    <svg class="portrait" viewBox="0 0 212 212" role="img" aria-label="Circular portrait photo of the presenter">
      <defs><linearGradient id="photoB" x1="0" y1="0" x2="0" y2="1"><stop offset="0" stop-color="#f4f2f1"/><stop offset="0.6" stop-color="#d9c5b6"/><stop offset="1" stop-color="#3b3a3c"/></linearGradient></defs>
      <circle cx="106" cy="106" r="105" fill="#dfa588"/>
      <circle cx="106" cy="106" r="101" fill="#9a1c22"/>
      <circle cx="106" cy="106" r="96" fill="#ffffff"/>
      <circle cx="106" cy="106" r="91" fill="url(#photoB)"/>
    </svg>
    <div class="brand"><span class="brand__dot"></span>Tall Reed Software</div>
    <footer class="footer"><span class="footer__page">01</span><span class="footer__date">01/02/15</span><span class="footer__start">Start</span></footer>
  </section>

  <section class="slide slide--c slide--blush">
    <div class="slide__header"></div>
    <div class="slide__rule"></div>
    <div class="slide__body"></div>
    <h1 class="slide__title">Project Title Here</h1>
    <p class="slide__subtitle">Subtext here Subtext here Subtext here Subtext here Subtext here Subtext here Subtext here Subtext here</p>
    <svg class="portrait" viewBox="0 0 212 212" role="img" aria-label="Circular portrait photo of the presenter">
      <defs><linearGradient id="photoC" x1="0" y1="0" x2="0" y2="1"><stop offset="0" stop-color="#f4f2f1"/><stop offset="0.6" stop-color="#d9c5b6"/><stop offset="1" stop-color="#3b3a3c"/></linearGradient></defs>
      <circle cx="106" cy="106" r="105" fill="#dfa588"/>
      <circle cx="106" cy="106" r="101" fill="#9a1c22"/>
      <circle cx="106" cy="106" r="96" fill="#ffffff"/>
      <circle cx="106" cy="106" r="91" fill="url(#photoC)"/>
    </svg>
    <div class="brand"><span class="brand__dot"></span>Tall Reed Software</div>
    <footer class="footer"><span class="footer__page">01</span><span class="footer__date">01/02/15</span><span class="footer__start">Start</span></footer>
  </section>

  <section class="slide slide--d slide--crimson">
    <div class="slide__header"></div>
    <div class="slide__rule"></div>
    <div class="slide__body"></div>
    <h1 class="slide__title">Project Title Here</h1>
    <p class="slide__subtitle">Subtext here Subtext here Subtext here Subtext here Subtext here<br>Subtext here Subtext here Subtext here</p>
    <div class="brand"><span class="brand__dot"></span>Tall Reed Software</div>
    <footer class="footer"><span class="footer__page">01</span><span class="footer__date">01/02/15</span><span class="footer__start">Start</span></footer>
  </section>

</main>
</body>
</html>
```